INFOGRAPHICS AND ICON DESIGN FOR PRINTING AND FINISHING COMPANY

We need to get an effective and customized INFOGRAPHIC with the intention to collect and show in the best way our company and figures. We mean included in the INFOGRAPHIC project also tne new design of our MILESTONE ( separated object).<br/>Overthat We need to get effective and customized ICON DESIGN following our brand identity and design of the new INFOGRAPHIC. All the projecs have to be scalable and modulated in order to be used whole or part of. Please have a look to our atthached brief to get all the information about the project for starting it.

Target Market(s)

Paper and Plastic converting company. Paper Packaging manufacturers. Publishing company of catalogues or collections of book which require of ennobled covers.

Colors

Designer to choose colors to be used in the design.

Requirements
Must have
• an effective and clear style which can immediately show who we are, what we do and the positioning of our company.
Nice to have
• Colors based on our brand identity. It means gradations of our brand colors and if impressive other colors but suited with them.
Should not have
• only set of standard icons and graphics with small changes. It means w need of creative design especially on the icon from where it will start our inforgraphic which must have to identify our company and positioning and market. It's not easy but not impossible!

```html
<!DOCTYPE html>
<html lang="en">
<head>
<meta charset="utf-8">
<title>Varesco — Company Figures Infographic</title>
<link href="https://fonts.googleapis.com/css2?family=Montserrat:wght@600;700;800&display=swap" rel="stylesheet">
<style>
  :root{
    --brand-blue:#386594;
    --paper:#ffffff;
    --halo:#eceef1;
    --icon-bg:#eef0f3;
    --steel:#b7b8ba;
    --steel-dark:#9fa1a4;
    --flag-green:#1f8a37;
    --flag-red:#c30d0d;
    --ink-light:#ffffff;
  }
  html,body{margin:0;padding:0;background:var(--paper);overflow:hidden;}
  .canvas{width:1200px;height:838px;display:block;}
  .frame{fill:none;stroke:var(--brand-blue);stroke-width:3.5;}
  .blob{fill:var(--brand-blue);}
  .halo{fill:var(--halo);}
  .icon-disc{fill:var(--icon-bg);stroke:var(--brand-blue);stroke-width:2;}
  .icon-disc-thick{fill:var(--icon-bg);stroke:var(--brand-blue);stroke-width:3;}
  .cat-disc{fill:var(--brand-blue);stroke:var(--paper);stroke-width:2;}
  .mini-disc{fill:var(--steel-dark);stroke:var(--paper);stroke-width:1.5;}
  .ring{fill:none;stroke:var(--brand-blue);stroke-width:5;}
  .connector{fill:none;stroke:var(--brand-blue);stroke-width:1.6;stroke-dasharray:1.6 2.6;stroke-linecap:round;}
  .tick{stroke:var(--brand-blue);stroke-width:1.8;}
  .underline{stroke:var(--ink-light);stroke-width:1.8;}
  text{font-family:'Montserrat',sans-serif;fill:var(--ink-light);font-weight:700;}
  .figure{font-weight:800;}
  .label{font-size:10.5px;font-weight:700;}
  .label-sm{font-size:6px;font-weight:700;}
  .label-xs{font-size:5px;font-weight:700;}
  .year{fill:var(--brand-blue);font-size:14px;font-weight:800;}
  .factory-body{fill:var(--steel);}
  .factory-accent{fill:var(--brand-blue);}
  .flag-green{fill:var(--flag-green);}
  .flag-white{fill:var(--paper);}
  .flag-red{fill:var(--flag-red);}
  .factory-base{fill:var(--steel);}
  .flag-text{fill:var(--brand-blue);font-size:10.5px;font-weight:700;}
  .brand-name{fill:var(--brand-blue);font-size:11px;font-weight:800;}
  .brand-dot{fill:var(--brand-blue);}
  .brand-pill{fill:var(--paper);}
</style>
</head>
<body>
<svg class="canvas" viewBox="0 0 1200 838" xmlns="http://www.w3.org/2000/svg">
  <rect class="frame" x="17" y="22" width="1165" height="792" rx="14"/>

  <!-- connectors -->
  <g class="connectors">
    <path class="connector" d="M181 209 v23 h127 v136 h52"/>
    <path class="connector" d="M383 162 v128 h69 v65"/>
    <path class="connector" d="M532 251 v83"/>
    <path class="connector" d="M692 222 v26 h-89 v112"/>
    <path class="connector" d="M764 295 v28 h-161"/>
    <path class="connector" d="M170 365 v20 q0 26 26 26 h164"/>
    <path class="connector" d="M630 410 h101 q8 0 10 -22 q2 -24 22 -24 h120"/>
    <path class="connector" d="M630 431 h35 v54 h63"/>
    <path class="connector" d="M368 476 v35 h-70"/>
    <path class="connector" d="M397 476 v64 h-82 v23"/>
    <path class="connector" d="M509 476 v55"/>
    <path class="connector" d="M588 476 v84 h42 v99"/>
    <path class="connector" d="M621 476 v71 h214 v20"/>
    <line class="tick" x1="175" y1="208" x2="187" y2="208"/>
    <line class="tick" x1="377" y1="161" x2="389" y2="161"/>
    <line class="tick" x1="526" y1="250" x2="538" y2="250"/>
    <line class="tick" x1="686" y1="221" x2="698" y2="221"/>
    <line class="tick" x1="758" y1="294" x2="770" y2="294"/>
    <line class="tick" x1="164" y1="364" x2="176" y2="364"/>
    <line class="tick" x1="884" y1="358" x2="884" y2="370"/>
    <line class="tick" x1="730" y1="479" x2="730" y2="491"/>
    <line class="tick" x1="297" y1="505" x2="297" y2="517"/>
    <line class="tick" x1="309" y1="564" x2="321" y2="564"/>
    <line class="tick" x1="503" y1="532" x2="515" y2="532"/>
    <line class="tick" x1="624" y1="660" x2="636" y2="660"/>
    <line class="tick" x1="829" y1="568" x2="841" y2="568"/>
  </g>

  <!-- 40 people -->
  <g class="stat stat-people">
    <circle class="blob" cx="172" cy="151" r="57"/>
    <g role="img" aria-label="Ring of team member icons">
      <circle class="icon-disc" cx="158" cy="91" r="15"/>
      <circle class="icon-disc" cx="197" cy="95" r="18"/>
      <circle class="icon-disc" cx="236" cy="117" r="18"/>
      <circle class="icon-disc" cx="248" cy="162" r="20"/>
      <circle class="icon-disc" cx="214" cy="145" r="10"/>
      <circle class="icon-disc" cx="222" cy="195" r="13"/>
      <circle class="icon-disc" cx="197" cy="198" r="7"/>
      <circle class="icon-disc" cx="158" cy="202" r="11"/>
      <circle class="icon-disc" cx="129" cy="186" r="13"/>
      <circle class="icon-disc" cx="112" cy="159" r="11"/>
      <circle class="icon-disc" cx="114" cy="134" r="9"/>
      <circle class="icon-disc" cx="130" cy="109" r="13"/>
    </g>
    <text class="figure" x="165" y="160" font-size="50" text-anchor="middle">40</text>
    <text class="label" x="186" y="180" font-size="12" text-anchor="middle">PEOPLE</text>
  </g>

  <!-- 60 years -->
  <g class="stat stat-history">
    <ellipse class="blob" cx="381" cy="104" rx="68" ry="50"/>
    <circle class="icon-disc" cx="310" cy="83" r="25"/>
    <text class="year" x="310" y="88" text-anchor="middle">1960</text>
    <circle class="icon-disc" cx="456" cy="89" r="31" role="img" aria-label="Ribbon-cutting icon"/>
    <text class="figure" x="376" y="95" font-size="32" text-anchor="middle">60</text>
    <text class="label" x="342" y="111">YEARS OF</text>
    <text class="label" x="342" y="125">EXPERIENCE</text>
    <text class="label" x="342" y="139">AND HISTORY</text>
  </g>

  <!-- foil printing -->
  <g class="stat stat-foil">
    <ellipse class="blob" cx="532" cy="198" rx="63" ry="45"/>
    <text class="label" x="580" y="184" text-anchor="end">HOT AND COLD</text>
    <text class="label" x="580" y="198" text-anchor="end">FOIL</text>
    <text class="label" x="580" y="212" text-anchor="end">PRINTING</text>
    <circle class="icon-disc-thick" cx="474" cy="229" r="38"/>
    <circle class="blob" cx="474" cy="227" r="24"/>
    <text class="label-sm" x="474" y="227" text-anchor="middle">MARKET</text>
    <text class="label-sm" x="474" y="235" text-anchor="middle">LEADER</text>
  </g>

  <!-- plants -->
  <g class="stat stat-plants">
    <ellipse class="blob" cx="686" cy="163" rx="65" ry="47"/>
    <circle class="icon-disc" cx="719" cy="115" r="34" role="img" aria-label="Two plant buildings icon"/>
    <text class="figure" x="665" y="190" font-size="58" text-anchor="middle">2</text>
    <text class="label" x="705" y="174" text-anchor="middle">PLANT</text>
    <text class="label" x="705" y="186" text-anchor="middle">IN</text>
    <text class="label" x="705" y="198" text-anchor="middle">ITALY</text>
  </g>
  <g class="stat stat-area">
    <ellipse class="blob" cx="765" cy="237" rx="67" ry="52"/>
    <text class="figure" x="759" y="222" font-size="28" text-anchor="middle">4500</text>
    <text class="label" x="715" y="239" font-size="11.5">SQM <tspan font-size="9">OF</tspan></text>
    <text class="label" x="715" y="253">PRODUCTION &amp;</text>
    <text class="label" x="718" y="267">WHAREHOUSE</text>
    <line class="underline" x1="726" y1="276" x2="792" y2="276"/>
  </g>
  <g class="illustration plant-view">
    <circle class="halo" cx="874" cy="175" r="78"/>
    <circle class="icon-disc-thick" cx="874" cy="175" r="70" role="img" aria-label="Illustration of the production plant building"/>
  </g>

  <!-- customers -->
  <g class="stat stat-customers">
    <ellipse class="blob" cx="172" cy="308" rx="63" ry="52"/>
    <circle class="halo" cx="99" cy="284" r="46"/>
    <circle class="icon-disc" cx="99" cy="284" r="42" role="img" aria-label="Crowd of customers icon"/>
    <text class="figure" x="186" y="312" font-size="32" text-anchor="middle">+500</text>
    <text class="label" x="184" y="328" font-size="11.5" text-anchor="middle">CUSTOMERS</text>
  </g>

  <!-- central factory -->
  <g class="factory">
    <rect class="factory-body" x="362" y="321" width="268" height="123" role="img" aria-label="Illustration of the company factory"/>
    <path class="factory-accent" d="M362 330 L436 444 L362 444 Z"/>
    <rect class="brand-pill" x="540" y="368" width="90" height="26" rx="13"/>
    <circle class="brand-dot" cx="555" cy="381" r="8"/>
    <text class="brand-name" x="567" y="385">VARESCO</text>
    <rect class="flag-green" x="362" y="444" width="85" height="21"/>
    <rect class="flag-white" x="447" y="444" width="90" height="21"/>
    <rect class="flag-red" x="537" y="444" width="93" height="21"/>
    <text class="flag-text" x="492" y="459" text-anchor="middle">Made in Italy</text>
    <rect class="factory-base" x="362" y="469" width="268" height="6"/>
  </g>

  <!-- markets ring -->
  <g class="stat stat-markets">
    <circle class="halo" cx="1013" cy="371" r="123"/>
    <circle class="ring" cx="1013" cy="371" r="107"/>
    <ellipse class="blob" cx="1010" cy="368" rx="70" ry="44"/>
    <text class="figure" x="1008" y="364" font-size="30" text-anchor="middle">+2000</text>
    <text class="label" x="1008" y="381" text-anchor="middle">GRAPHIC SUBJECTS</text>
    <text class="label" x="1008" y="395" text-anchor="middle">MANAGED</text>
    <text class="label" x="1008" y="409" text-anchor="middle">EVERY YEAR</text>
    <circle class="mini-disc" cx="1082" cy="387" r="15"/>
    <circle class="mini-disc" cx="1064" cy="415" r="15"/>
    <circle class="mini-disc" cx="1034" cy="430" r="15"/>
    <circle class="mini-disc" cx="997" cy="432" r="15"/>
    <g class="categories">
      <circle class="cat-disc" cx="962" cy="272" r="26"/><text class="label-xs" x="962" y="291" text-anchor="middle">ADHESIVES</text>
      <circle class="cat-disc" cx="1030" cy="267" r="26"/><text class="label-xs" x="1030" y="274" text-anchor="middle">BEAUTY</text><text class="label-xs" x="1030" y="281" text-anchor="middle">PRODUCTS</text>
      <circle class="cat-disc" cx="1091" cy="296" r="26"/><text class="label-xs" x="1091" y="295" text-anchor="middle">ASSEMBLY</text><text class="label-xs" x="1091" y="302" text-anchor="middle">AND</text><text class="label-xs" x="1091" y="309" text-anchor="middle">PUBLICATION</text>
      <circle class="cat-disc" cx="911" cy="324" r="26"/><text class="label-xs" x="911" y="338" text-anchor="middle">LIQUEURS</text>
      <circle class="cat-disc" cx="1121" cy="359" r="26"/><text class="label-xs" x="1121" y="364" text-anchor="middle">PHARMACEUTICAL</text><text class="label-xs" x="1121" y="370" text-anchor="middle">PRODUCTS</text>
      <circle class="cat-disc" cx="900" cy="407" r="26"/><text class="label-xs" x="900" y="415" text-anchor="middle">CONSUMER</text><text class="label-xs" x="900" y="422" text-anchor="middle">GOODS</text>
      <circle class="cat-disc" cx="939" cy="460" r="26"/><text class="label-xs" x="939" y="476" text-anchor="middle">JEWELERY</text>
    </g>
    <circle class="halo" cx="1045" cy="507" r="45"/>
    <circle class="icon-disc" cx="1045" cy="507" r="40"/>
    <g style="fill:var(--brand-blue)">
      <text class="label-sm" x="1045" y="488" text-anchor="middle" style="fill:var(--brand-blue);font-size:8.5px"><tspan font-size="12">1</tspan> MILION</text>
      <text class="label-sm" x="1045" y="499" text-anchor="middle" style="fill:var(--brand-blue);font-size:8.5px">OF SQM</text>
      <text class="label-sm" x="1045" y="510" text-anchor="middle" style="fill:var(--brand-blue);font-size:8.5px">OF FOIL FOR</text>
      <text class="label-sm" x="1045" y="521" text-anchor="middle" style="fill:var(--brand-blue);font-size:8.5px">PRINTING</text>
      <text class="label-sm" x="1045" y="532" text-anchor="middle" style="fill:var(--brand-blue);font-size:8.5px">IN STOCKL</text>
    </g>
  </g>

  <!-- technical support -->
  <g class="stat stat-support">
    <ellipse class="blob" cx="780" cy="487" rx="50" ry="41"/>
    <circle class="halo" cx="847" cy="490" r="34"/>
    <circle class="icon-disc" cx="847" cy="490" r="30" role="img" aria-label="Engineer with gear icon"/>
    <text class="label" x="780" y="481" text-anchor="middle">TECHNICAL</text>
    <text class="label" x="780" y="493" text-anchor="middle">PROJECT</text>
    <text class="label" x="780" y="505" text-anchor="middle">SUPPORT</text>
  </g>

  <!-- printing hours -->
  <g class="stat stat-hours">
    <ellipse class="blob" cx="222" cy="512" rx="70" ry="52"/>
    <circle class="halo" cx="119" cy="514" r="43"/>
    <circle class="icon-disc-thick" cx="119" cy="514" r="39" role="img" aria-label="Foil roll with clock icon"/>
    <text class="figure" x="222" y="507" font-size="26" text-anchor="middle">+100000</text>
    <text class="label" x="227" y="523" text-anchor="middle">OF PRINTING HOURS</text>
    <text class="label" x="224" y="537" text-anchor="middle">EVERY YEAR</text>
    <line class="underline" x1="198" y1="546" x2="250" y2="546"/>
  </g>

  <!-- machines -->
  <g class="stat stat-machines">
    <ellipse class="blob" cx="311" cy="621" rx="70" ry="52"/>
    <text class="figure" x="296" y="607" font-size="26" text-anchor="middle">14</text>
    <text class="label" x="304" y="620" text-anchor="middle">AUTOMATICAND</text>
    <text class="figure" x="298" y="644" font-size="26" text-anchor="middle">10</text>
    <text class="label" x="300" y="656" text-anchor="middle">MANUAL</text>
    <circle class="icon-disc" cx="371" cy="647" r="27"/>
    <text class="label-sm" x="372" y="646" text-anchor="middle" style="fill:var(--brand-blue);font-size:8px">PRINTING</text>
    <text class="label-sm" x="372" y="655" text-anchor="middle" style="fill:var(--brand-blue);font-size:8px">MACHINES</text>
    <circle class="halo" cx="140" cy="682" r="68"/>
    <circle class="icon-disc-thick" cx="140" cy="682" r="62" role="img" aria-label="Illustration of an automatic foil printing line"/>
    <circle class="halo" cx="252" cy="730" r="54"/>
    <circle class="icon-disc-thick" cx="252" cy="730" r="49" role="img" aria-label="Illustration of a multi-colour printing press"/>
    <circle class="halo" cx="339" cy="706" r="37"/>
    <circle class="icon-disc-thick" cx="339" cy="706" r="33" role="img" aria-label="Illustration of a manual printing machine"/>
  </g>

  <!-- tools -->
  <g class="stat stat-tools">
    <ellipse class="blob" cx="509" cy="598" rx="78" ry="57"/>
    <text class="figure" x="506" y="580" font-size="30" text-anchor="middle">+3000</text>
    <text class="label" x="510" y="594" text-anchor="middle">PRINTING TOOL</text>
    <text class="label" x="508" y="608" text-anchor="middle">IN WHAREHOUSE</text>
    <text class="label" x="508" y="622" text-anchor="middle">MANAGED FRO</text>
    <text class="label" x="510" y="636" text-anchor="middle">OUR CUSTOMERS</text>
    <circle class="halo" cx="479" cy="674" r="33"/>
    <circle class="icon-disc" cx="479" cy="674" r="29" role="img" aria-label="Engraved printing plate icon"/>
  </g>

  <!-- sheets -->
  <g class="stat stat-sheets">
    <ellipse class="blob" cx="632" cy="720" rx="65" ry="52"/>
    <text class="figure" x="632" y="711" font-size="27" text-anchor="middle">+50Mn</text>
    <text class="label" x="632" y="726" text-anchor="middle">OF</text>
    <text class="label" x="634" y="738" text-anchor="middle">PRINTED SHEETS</text>
    <text class="label" x="634" y="750" text-anchor="middle">EVERY YEARS</text>
    <circle class="halo" cx="729" cy="724" r="43"/>
    <circle class="icon-disc-thick" cx="729" cy="724" r="38" role="img" aria-label="Stacks of printed sheets icon"/>
  </g>

  <!-- graphic subjects -->
  <g class="stat stat-graphics">
    <ellipse class="blob" cx="837" cy="627" rx="73" ry="52"/>
    <text class="figure" x="833" y="616" font-size="30" text-anchor="middle">+2000</text>
    <text class="label" x="833" y="633" text-anchor="middle">GRAPHIC SUBJECTS</text>
    <text class="label" x="833" y="647" text-anchor="middle">MANAGED</text>
    <text class="label" x="835" y="661" text-anchor="middle">EVERY YEAR</text>
    <circle class="halo" cx="915" cy="672" r="41"/>
    <circle class="icon-disc-thick" cx="915" cy="672" r="36" role="img" aria-label="Artwork proof with colour wheel icon"/>
  </g>
</svg>
</body>
</html>
```